11 x 11 Flyer Design for Social Media - Reverse Mortgages

62 or older?

A Reverse Mortgage
could be
Your Road to Financial Freedom

* No Monthly Payments
* No Income Requirements
* No Credit Score Requirements
* No Loss of Ownership

Receive cash by lump sum, monthly installments or a line of credit!!

Call us today for a Free Consultation!!
(800) 471-2965

Bluegate Financial Services, Inc.
NMLS #318760
www.bluegatehome.com

```html
<!DOCTYPE html>
<html lang="en">
<head>
<meta charset="utf-8">
<title>Reverse Mortgage Flyer</title>
<link href="https://fonts.googleapis.com/css2?family=Montserrat:wght@400;500;600;700;800;900&family=Saira+Semi+Condensed:wght@700&display=swap" rel="stylesheet">
<style>
  :root{
    --olive:#a79a33;
    --olive-light:#c9bd6a;
    --beige:#e2dcaa;
    --blue:#1b5fa9;
    --green:#9dc73b;
    --white:#ffffff;
    --ink:#333333;
    --gold:#b2a23a;
  }
  html,body{margin:0;padding:0;overflow:hidden;background:#fff;}
  .flyer{position:relative;width:1200px;height:1200px;overflow:hidden;
    background:linear-gradient(90deg,var(--olive) 0%,var(--olive) 55%,var(--olive-light) 100%);
    font-family:"Montserrat",sans-serif;}
  .photo-couple-top{position:absolute;left:760px;top:0;width:440px;height:380px;
    background:linear-gradient(90deg,rgba(201,189,106,0) 0%,#c8c49a 30%,#d9dccf 70%,#e6e8e0 100%);}
  .layer{position:absolute;left:0;top:0;width:1200px;height:1200px;}
  .wave-fill{z-index:0;}
  .wave-line{z-index:3;}
  .intro-tag{position:absolute;left:61px;top:47px;width:355px;height:75px;background:var(--white);
    color:var(--blue);font-weight:900;font-size:43px;letter-spacing:-1px;line-height:75px;text-align:center;z-index:2;}
  .intro-line{position:absolute;left:423px;color:var(--white);font-weight:600;font-size:37px;line-height:1;letter-spacing:.5px;z-index:2;}
  .headline{position:absolute;left:70px;top:122px;margin:0;color:var(--white);font-weight:900;
    font-size:112px;line-height:97px;letter-spacing:-3px;text-shadow:3px 3px 4px rgba(0,0,0,.35);z-index:2;}
  .photo-couple-bottom{position:absolute;left:0;top:470px;width:340px;height:386px;z-index:1;
    background:linear-gradient(135deg,#4a3a33 0%,#7a5a45 45%,#e9e6e0 100%);
    clip-path:polygon(75px 0,321px 30px,210px 386px,0 386px,0 90px);}
  .gold-stripe{z-index:1;}
  .cash-offer{position:absolute;left:365px;top:570px;margin:0;color:var(--blue);font-size:37px;line-height:38.5px;font-weight:500;z-index:2;}
  .cash-offer strong{font-weight:900;}
  .benefits{position:absolute;left:700px;top:340px;width:444px;height:541px;background:var(--green);z-index:2;
    clip-path:polygon(0 105px,171px 40px,295px 10px,444px 5px,444px 100%,0 100%);}
  .benefit{position:absolute;left:0;width:444px;height:100px;}
  .benefit svg{position:absolute;left:27px;top:14px;}
  .benefit span{position:absolute;left:116px;top:10px;color:var(--white);font-family:"Saira Semi Condensed",sans-serif;
    font-weight:700;font-size:38px;line-height:42px;text-shadow:2px 2px 3px rgba(0,0,0,.35);white-space:nowrap;}
  .benefit-rule{position:absolute;left:30px;width:370px;border-top:2px dashed rgba(255,235,120,.8);}
  .footer{position:absolute;left:0;top:856px;width:1200px;height:284px;background:var(--white);z-index:1;}
  .brand{position:absolute;left:40px;top:110px;display:flex;align-items:center;gap:14px;
    color:var(--blue);font-weight:700;font-size:24px;line-height:30px;}
  .brand i{display:block;flex:none;width:30px;height:30px;border-radius:50%;background:var(--blue);}
  .cta{position:absolute;right:32px;text-align:right;color:var(--blue);font-weight:900;margin:0;letter-spacing:-.5px;}
  .cta-call{top:35px;font-size:47px;}
  .cta-free{top:90px;font-size:55px;}
  .cta-rule{position:absolute;left:995px;top:167px;width:173px;height:9px;background:var(--blue);}
  .phone-icon{position:absolute;left:413px;top:188px;}
  .phone-number{position:absolute;right:32px;top:178px;color:var(--ink);font-weight:800;font-size:88px;letter-spacing:-1px;line-height:1;}
  .legal-bar{position:absolute;left:0;top:1140px;width:1200px;height:60px;background:var(--blue);z-index:4;
    color:var(--white);display:flex;align-items:center;justify-content:center;gap:22px;}
  .legal-bar .company{font-size:23px;font-weight:400;}
  .legal-bar .sep{width:4px;height:32px;background:var(--white);}
  .legal-bar .url{font-size:28px;font-weight:700;}
</style>
</head>
<body>
<main class="flyer">
  <div class="photo-couple-top" role="img" aria-label="Photo of a smiling senior couple on a beach"></div>

  <svg class="layer wave-fill" viewBox="0 0 1200 1200" aria-hidden="true">
    <path d="M0,392 C200,520 430,560 700,445 S1050,340 1200,345 V1200 H0 Z" fill="var(--beige)"/>
  </svg>

  <div class="intro-tag">62 OR OLDER?</div>
  <div class="intro-line" style="top:52px">A REVERSE MORTGAGE</div>
  <div class="intro-line" style="top:88px">COULD BE</div>
  <h1 class="headline">YOUR ROAD<br>TO FINANCIAL<br>FREEDOM</h1>

  <svg class="layer gold-stripe" viewBox="0 0 1200 1200" aria-hidden="true">
    <polygon points="340,560 339,610 270,790 230,800" fill="var(--gold)"/>
  </svg>
  <div class="photo-couple-bottom" role="img" aria-label="Photo of a laughing senior couple taking a selfie"></div>

  <p class="cash-offer"><strong>RECEIVE CASH</strong><br>BY LUMP SUM,<br>MONTHLY<br>INSTALLMENTS<br>OR A LINE OF<br>CREDIT!!</p>

  <section class="benefits">
    <div class="benefit" style="top:111px"><svg width="74" height="74" viewBox="0 0 74 74" aria-hidden="true"><circle cx="37" cy="37" r="33" fill="none" stroke="#fff" stroke-width="5"/><path d="M20,38 L32,50 L54,26" fill="none" stroke="#fff" stroke-width="6" stroke-linecap="round" stroke-linejoin="round"/></svg><span>No Credit Score<br>Requirements</span></div>
    <div class="benefit-rule" style="top:217px"></div>
    <div class="benefit" style="top:214px"><svg width="74" height="74" viewBox="0 0 74 74" aria-hidden="true"><circle cx="37" cy="37" r="33" fill="none" stroke="#fff" stroke-width="5"/><path d="M20,38 L32,50 L54,26" fill="none" stroke="#fff" stroke-width="6" stroke-linecap="round" stroke-linejoin="round"/></svg><span>No Loss of<br>Ownership</span></div>
    <div class="benefit-rule" style="top:319px"></div>
    <div class="benefit" style="top:320px"><svg width="74" height="74" viewBox="0 0 74 74" aria-hidden="true"><circle cx="37" cy="37" r="33" fill="none" stroke="#fff" stroke-width="5"/><path d="M20,38 L32,50 L54,26" fill="none" stroke="#fff" stroke-width="6" stroke-linecap="round" stroke-linejoin="round"/></svg><span style="left:106px">No Monthly<br>Payments</span></div>
    <div class="benefit-rule" style="top:423px"></div>
    <div class="benefit" style="top:426px"><svg width="74" height="74" viewBox="0 0 74 74" aria-hidden="true"><circle cx="37" cy="37" r="33" fill="none" stroke="#fff" stroke-width="5"/><path d="M20,38 L32,50 L54,26" fill="none" stroke="#fff" stroke-width="6" stroke-linecap="round" stroke-linejoin="round"/></svg><span>No Income<br>Requirements</span></div>
  </section>

  <svg class="layer wave-line" viewBox="0 0 1200 1200" aria-hidden="true">
    <path d="M0,392 C200,520 430,560 700,445 S1050,340 1200,345" fill="none" stroke="var(--blue)" stroke-width="18"/>
    <path d="M665,385 C720,320 820,330 875,415" fill="none" stroke="#2b2b2b" stroke-width="6" stroke-linecap="round"/>
    <path d="M880,380 L880,455 L827,416 Z" fill="#2b2b2b"/>
  </svg>

  <footer class="footer">
    <div class="brand"><i></i><span>Bluegate Financial<br>Services, Inc.</span></div>
    <p class="cta cta-call">CALL US TODAY</p>
    <p class="cta cta-free">FREE CONSULTATION!!</p>
    <div class="cta-rule"></div>
    <svg class="phone-icon" width="84" height="84" viewBox="0 0 84 84" aria-hidden="true">
      <path d="M14,10 L28,8 L34,26 L25,32 C30,44 40,54 52,59 L58,50 L76,56 L74,70 C70,76 60,78 50,74 C32,66 18,52 10,34 C6,24 8,14 14,10 Z" fill="none" stroke="var(--ink)" stroke-width="5" stroke-linejoin="round"/>
      <path d="M48,30 A8,8 0 0 1 55,37 M48,20 A18,18 0 0 1 65,37 M48,10 A28,28 0 0 1 75,37" fill="none" stroke="var(--ink)" stroke-width="5" stroke-linecap="round"/>
    </svg>
    <div class="phone-number">(800) 471-2965</div>
  </footer>

  <div class="legal-bar">
    <span class="company">Bluegate Financial Services, Inc. NMLS #318760</span>
    <span class="sep"></span>
    <span class="url">www.bluegatehome.com</span>
  </div>
</main>
</body>
</html>
```